Chewable Dog Supplements jar with lid

Below are some specifications of this project: 
There will be 6 different types of dog supplements in different jars, which will have different colors, or elements(dogs),  but will respect the same theme overall.  I attached some pictures below as a reference.
 The design I would like to create is for a label that will go around and on the top of a round plastic jar. The size of the product label is 25cm long and 8.5 cm high and on the top there is a circle that goes on the lid with the exact same design as on the front.
Some small pictures on the back with no Grain, Corn or Soy derivates  
 All products come in different shapes chews 
All products have 3 different headlines with their benefits that go on the front of the design.
All products have different flavors.
Regarding the text that will go on the back of the product, I can help with adding that to all products as long as we agree on how it looks. On the back I will need a space for a barcode, best before date, there should be 2 tables with ingredients and directions for use, and space for text under :Storage instructions, Warning, Description.

Target Market(s)

Europe

Industry/Entity Type

pet food

Requirements
Must have
• Trust signals ( Free from GMO, Natural ingredients, Free from artificial colouring) and a text box with the benefits of the product that I will provide.

```html
<!DOCTYPE html>
<html lang="en">
<head>
<meta charset="utf-8">
<title>Multivitamin Chews – wrap label</title>
<link href="https://fonts.googleapis.com/css2?family=Arimo:wght@400;700&family=Roboto+Condensed:ital,wght@0,700;1,800;1,900&family=Roboto+Slab:wght@500&display=swap" rel="stylesheet">
<style>
  :root{
    --page:#ecebe8;
    --white:#ffffff;
    --red:#c6232b;
    --orange:#d9571f;
    --navy:#1f2a6b;
    --title-blue:#2a76c6;
    --yellow:#efe41a;
    --table:#6c6db4;
    --table-dark:#4c4d98;
    --slate:#3b424b;
    --ink:#1e1e1e;
    --green:#8dbb4a;
  }
  *{margin:0;padding:0;box-sizing:border-box}
  html,body{width:979px;height:1200px;overflow:hidden;background:var(--page)}
  body{position:relative;font-family:"Arimo",Arial,sans-serif;color:var(--ink)}
  .label{position:absolute;left:0;top:503px;width:1395px;height:272px;transform:scale(0.7018);transform-origin:0 0;background:var(--white);overflow:hidden}
  .label-bg{position:absolute;left:0;top:0}
  .abs{position:absolute}
  .panel-heading{font:700 13px "Arimo",Arial,sans-serif;color:var(--ink);letter-spacing:.2px}
  .facts-table{position:absolute;top:47px;width:215px;height:210px;background:var(--table);border:3px solid var(--table-dark);border-radius:6px;color:#fff;font-size:9.4px;padding:4px 6px}
  .facts-table .head{font-weight:700;border-bottom:1px solid #fff;padding-bottom:3px;margin-bottom:3px}
  .facts-table .row{display:flex;justify-content:space-between;line-height:11.2px;white-space:nowrap}
  .facts-table .row span:first-child{overflow:hidden;text-overflow:clip}
  .facts-table .inactive{border-top:2px solid #fff;margin-top:5px;padding-top:3px;line-height:10.2px}
  .title{font:italic 900 34px/34px "Roboto Condensed",sans-serif;color:var(--title-blue);text-align:center;-webkit-text-stroke:1px var(--navy);letter-spacing:-.5px;white-space:nowrap}
  .count-badge{left:826px;top:0;width:72px;height:52px;background:var(--slate);border-radius:0 0 10px 10px;color:#fff;text-align:center;padding-top:14px}
  .count-badge small{display:block;font-size:6.5px;line-height:8px}
  .count-badge strong{display:block;font:italic 800 13px/15px "Roboto Condensed",sans-serif}
  .brand-name{left:812px;top:117px;width:110px;text-align:center;font:700 10px "Arimo",Arial,sans-serif;letter-spacing:3px;color:var(--ink)}
  .benefit-box{left:806px;top:159px;width:118px;height:56px;background:var(--yellow);border-radius:3px;text-align:center;font:500 9px/11px "Roboto Slab",serif;color:var(--ink);padding-top:2px}
  .benefit-box p{border-bottom:1px solid #8b8520;margin:0 8px;padding:2px 0}
  .benefit-box p:last-of-type{border:none;padding-bottom:0}
  .benefit-box small{display:block;font-size:4.5px;line-height:5px;color:#555}
  .digest{left:828px;top:222px;font-size:6.5px;line-height:8px;color:#fff}
  .digest b{font-size:8px;display:block;color:var(--ink)}
  .support{left:758px;top:251px;font:italic 800 9px "Roboto Condensed",sans-serif;color:#fff}
  .salmon-text{left:572px;top:220px;font-size:8px;color:#fff;line-height:9px}
  .salmon-text b{font-size:10px}
  .net-wt{left:572px;top:252px;font-size:5.5px;color:#fff}
  .back-copy{font-size:8.2px;line-height:9.6px;color:var(--ink);text-align:justify}
  .back-copy h4{font-size:8.2px;font-weight:400}
  .on-red{color:#fbe3d8}
  .code-box{left:970px;top:216px;width:170px;height:40px;background:#fff}
</style>
</head>
<body>
<section class="label" aria-label="Multivitamin Chews wrap label">
  <svg class="label-bg" viewBox="0 0 1395 272" width="1395" height="272" aria-hidden="true">
    <defs>
      <linearGradient id="frontFill" x1="0" x2="1" y1="0" y2="0">
        <stop offset="0" stop-color="var(--orange)"/>
        <stop offset=".7" stop-color="#d2461f"/>
        <stop offset="1" stop-color="var(--red)"/>
      </linearGradient>
    </defs>
    <polygon points="0,28 540,42 540,272 0,272" fill="var(--red)"/>
    <path d="M540,272 L540,150 C640,138 760,150 860,140 C900,136 935,130 960,126 L960,272 Z" fill="url(#frontFill)"/>
    <polygon points="960,272 960,205 1155,198 1155,118 1395,22 1395,272" fill="var(--red)"/>
    <circle cx="697" cy="187" r="86" fill="var(--yellow)"/>
    <circle cx="693" cy="187" r="84" fill="var(--navy)"/>
    <circle cx="697" cy="187" r="77" fill="#eaeaea"/>
    <circle cx="827" cy="147" r="13" fill="var(--navy)"/>
    <circle cx="864" cy="147" r="13" fill="var(--navy)"/>
    <circle cx="900" cy="147" r="13" fill="var(--navy)"/>
    <path d="M821,147 h12 M827,141 v12" stroke="#fff" stroke-width="2"/>
    <path d="M860,140 v14 M868,140 v14" stroke="#fff" stroke-width="2"/>
    <path d="M895,152 a5,5 0 0 1 10,0" stroke="#fff" stroke-width="2" fill="none"/>
  </svg>

  <h2 class="abs panel-heading" style="left:70px;top:24px">PRODUCT FACTS</h2>
  <h2 class="abs panel-heading" style="left:274px;top:24px">INFORMATII DESPRE PRODUS</h2>

  <div class="facts-table" style="left:35px">
    <div class="head">Active Ingredients per 1 Soft Chew (2.5g):</div>
    <div class="row"><span>Organic Hemp Seed Oil</span><span>200 mg</span></div>
    <div class="row"><span>Organic Hemp Seed Powder</span><span>200 mg</span></div>
    <div class="row"><span>Organic Chamomile</span><span>200 mg</span></div>
    <div class="row"><span>Colostrum</span><span>200 mg</span></div>
    <div class="row"><span>Organic Passion Flower</span><span>120 mg</span></div>
    <div class="row"><span>L-Tryptophan 98%</span><span>90 mg</span></div>
    <div class="row"><span>Valerian Root</span><span>80 mg</span></div>
    <div class="row"><span>Organic Ginger Root Powder</span><span>80 mg</span></div>
    <div class="row"><span>Ashwagandha</span><span>50 mg</span></div>
    <div class="row"><span>Vitamin B1</span><span>25 mg</span></div>
    <div class="inactive">Inactive Ingredients: Natural Beef Flavor, Sunflower Lecithin, Flaxseed, Coconut Glycerin, Powdered Cellulose, Rosemary Extract, Mixed Tocopherols, Garbanzo Flour, Sweet Potato, Carrot, Pea Flour, Sorbic Acid.</div>
  </div>

  <div class="facts-table" style="left:256px;width:222px">
    <div class="head">Active Ingredients per 1 Soft Chew (2.5g):</div>
    <div class="row"><span>(Ulei de semințe de cânepă organică)</span><span>200 mg</span></div>
    <div class="row"><span>(Pudră de semințe de cânepă organică)</span><span>200 mg</span></div>
    <div class="row"><span>(Mușețel organic)</span><span>200 mg</span></div>
    <div class="row"><span>(Colostru)</span><span>200 mg</span></div>
    <div class="row"><span>(Floare de pasiune organică)</span><span>120 mg</span></div>
    <div class="row"><span>(L-Triptofan 98%)</span><span>90 mg</span></div>
    <div class="row"><span>(Rădăcină de valeriană)</span><span>80 mg</span></div>
    <div class="row"><span>(Pudră de rădăcină de ghimbir organic)</span><span>80 mg</span></div>
    <div class="row"><span>(Ashwagandha)</span><span>50 mg</span></div>
    <div class="row"><span>(Vitamina B1)</span><span>25 mg</span></div>
    <div class="inactive">Ingrediente inactive: Aromă naturală de carne de vită, lecitină de floarea-soarelui, semințe de in, glicerină de cocos, celuloză sub formă de pudră, extract de rozmarin, amestec de tocoferoli, făină de garbanzo, cartof dulce, morcov, făină de mazăre, acid sorbic.</div>
  </div>

  <h1 class="abs title" style="left:595px;top:26px;width:200px">Multivitamin<br>Chews</h1>
  <div class="abs count-badge"><small>Gluten Free Soft</small><strong>60 CHEWS</strong></div>

  <div class="abs" role="img" aria-label="Hand-lettered 'Natural product 100%' seal with leaf" style="left:556px;top:70px;width:66px;height:56px;border-radius:50%;background:rgba(141,187,74,.2)"></div>
  <div class="abs" role="img" aria-label="Photo of a smiling black and white border collie" style="left:625px;top:115px;width:144px;height:144px;border-radius:50%;background:radial-gradient(circle at 50% 45%,#6a6460,#2a2624 70%)"></div>
  <div class="abs" role="img" aria-label="Line drawing of a seated puppy" style="left:843px;top:74px;width:44px;height:36px;background:#f2f2f2;border-radius:6px"></div>
  <div class="abs brand-name">PAWNOVA</div>

  <div class="abs benefit-box">
    <p>Strong Immunity</p>
    <p>Hip And Joint Support</p>
    <p>Skin And Coat Health</p>
    <small>+ Vitamin E &amp; Omega</small>
  </div>

  <div class="abs" role="img" aria-label="Illustration of a leaping salmon" style="left:548px;top:208px;width:22px;height:42px;border-radius:40%;background:linear-gradient(#f0c3a8,#c7785a)"></div>
  <div class="abs salmon-text">Real<br><b>Salmon</b><br>Ingredient</div>
  <div class="abs net-wt">NET WT 5.29 OZ(150g)</div>

  <div class="abs" role="img" aria-label="Photo of two brown soft chews" style="left:764px;top:204px;width:58px;height:42px;border-radius:10px;background:linear-gradient(135deg,#7a5a34,#3e2a16)"></div>
  <div class="abs digest"><b>HIGHLY DIGESTIBLE</b>100% nutrition 1 0% fillers<br>&nbsp;&nbsp;&nbsp;Every ingredient has a purpose</div>
  <div class="abs support">SUPPORT FOR DOGS</div>

  <div class="abs back-copy" style="left:970px;top:36px;width:175px">
    <h4>CAUTIONS(PRECAUȚII):</h4>
    Safe use in pregnant animals or animals intended for breeding has not been proven. If animal's condition worsens, discontinue use and contact your veterinarian Administer during or after animal has eaten to reduce incidence of gastrointestinal upset.
    <h4 style="margin-top:6px">WARNINGS(AVERTISMENTE):</h4>
    Keep out of the reach of children and other animals. In case of accidental ingestion or overdose contact health professional immediately.
    <p style="margin-top:7px">Importator:<br>Ferrowick Trade Ltd Str. Lindenweg 12<br>info@pawnova.example<br>pawnova.example</p>
  </div>
  <div class="abs code-box"></div>

  <div class="abs back-copy" style="left:1175px;top:36px;width:175px">
    Product Facts (Continued)<br>For use in dogs only<br>Directions for Use:<br>
    Begin with half the suggested amount and gradually increase to the suggested daily amount. Amounts can be split between AM and PM.
  </div>
  <div class="abs back-copy on-red" style="left:1175px;top:155px;width:175px">
    <h4>STORAGE(DEPOZITARE):</h4>
    Store in a cool, dry place. Do not freeze.<br>(A se păstra într-un loc răcoros și uscat.)
  </div>
</section>
</body>
</html>
```